Business card for a plastic surgeon

i need a business card for a plastic surgeon. I have two adresses. The card should communicate safety, simmetry, beauty and with soft colors.
What i want in the card:
- my logo: Letters "R"and "B" (picture uploaded)
- my name: Renato Bastiani
- my registration: CRM 507 219
- my adresses and phone numbers (2):
- Av Dr Teixeira Lopes, 2710, sala 305 - Vila Olímpia | São Paulo/ SP - Phone: 11 4172-5036
- Al. Itapeva, 47, 3 andar - Alphaville | Barueri/ SP - Phone: 11 6350-2481

- my social network: site, facebook and instagram

Target Market(s)

people (95% girls and women) that want cosmetic procedures and plastic surgery

Industry/Entity Type

Business

Contact Information for Business Card

The card should communicate safety, simmetry, beauty and with soft colors.
Beige, brown, gray, rosy are some options. Color is free

Font styles to use
Serif

Requirements
Must have
• - my logo: Letters "R"and "B" (picture uploaded)
• - my name: Renato Bastiani
• - my registration: CRM 507 219
• - my adresses and phone numbers (2):
• - Av Dr Teixeira Lopes, 2710, sala 305 - Vila Olímpia | São Paulo/ SP - Phone: 11 4172-5036
• - Al. Itapeva, 47, 3 andar - Alphaville | Barueri/ SP - Phone: 11 6350-2481
• - my social network: site, facebook and instagram
Should not have
• other images (only my logo)

```html
<!DOCTYPE html>
<html lang="pt-BR">
<head>
<meta charset="utf-8">
<title>Renato Bastiani – Cartão de visita</title>
<link rel="stylesheet" href="https://fonts.googleapis.com/css2?family=Lato:wght@300;700&family=Montserrat:wght@400;500&display=swap">
<style>
  :root {
    --backdrop: #ece7e2;
    --card-white: #ffffff;
    --beige: #ead2bc;
    --beige-deep: #e2c3a6;
    --ink: #5f5f5f;
    --ink-soft: #9a9a9a;
    --mark: #c9b29c;
  }
  * { margin: 0; padding: 0; box-sizing: border-box; }
  html, body { width: 1200px; height: 1000px; overflow: hidden; }
  body {
    background: var(--backdrop);
    font-family: "Montserrat", sans-serif;
    color: var(--ink);
    position: relative;
  }
  .card {
    position: absolute;
    left: 300px;
    width: 600px;
    height: 340px;
    border-radius: 28px;
    overflow: hidden;
    box-shadow: 0 6px 18px rgba(0,0,0,.12);
  }
  .card-front { top: 110px; background: var(--card-white); }
  .card-back { top: 550px; background: var(--beige); }
  .front-wave { position: absolute; inset: 0; }

  .identity { position: absolute; left: 46px; top: 112px; display: flex; align-items: center; gap: 18px; }
  .monogram {
    font-family: "Lato", sans-serif; font-weight: 300;
    font-size: 38px; color: var(--mark); letter-spacing: 1px;
  }
  .doctor-name { font-family: "Lato", sans-serif; font-weight: 700; font-size: 25px; color: var(--ink); }
  .registration { font-family: "Lato", sans-serif; font-weight: 300; font-size: 16px; color: var(--ink-soft); margin-top: 2px; }

  .social { position: absolute; right: 44px; top: 60px; display: flex; align-items: center; gap: 12px; }
  .social-dot { width: 30px; height: 30px; border-radius: 50%; background: var(--beige); }
  .social-handle { font-size: 15px; color: var(--ink); }

  .contact { position: absolute; font-size: 13px; line-height: 1.55; color: var(--ink); }
  .contact-row { display: flex; align-items: flex-start; gap: 8px; }
  .contact-row svg { flex: none; width: 14px; height: 14px; margin-top: 2px; fill: var(--ink); }
  .contact-barueri { right: 36px; top: 222px; }
  .contact-saopaulo { left: 40px; top: 262px; }

  .back-name {
    position: absolute; left: 0; right: 0; top: 118px; text-align: center;
    font-family: "Lato", sans-serif; font-weight: 300; font-size: 40px; color: var(--ink);
  }
  .website {
    position: absolute; left: 0; right: 0; bottom: 28px; text-align: center;
    font-size: 15px; color: var(--ink);
  }
</style>
</head>
<body>

<section class="card card-front">
  <svg class="front-wave" viewBox="0 0 600 340" preserveAspectRatio="none" aria-hidden="true">
    <path d="M0,340 L0,255 C160,200 360,170 600,140 L600,340 Z" fill="var(--beige)"/>
    <path d="M330,196 C440,182 530,168 600,150 C530,178 440,192 330,196 Z" fill="var(--card-white)"/>
  </svg>

  <div class="identity">
    <span class="monogram">RB</span>
    <div>
      <h1 class="doctor-name">Renato Bastiani</h1>
      <p class="registration">CRM 507 219</p>
    </div>
  </div>

  <div class="social">
    <span class="social-dot"></span>
    <span class="social-handle">RenatoBastiani</span>
  </div>

  <div class="contact contact-barueri">
    <div class="contact-row">
      <svg viewBox="0 0 24 24"><path d="M6.6 10.8c1.4 2.8 3.8 5.1 6.6 6.6l2.2-2.2c.3-.3.7-.4 1-.2 1.1.4 2.3.6 3.6.6.6 0 1 .4 1 1V20c0 .6-.4 1-1 1C10.6 21 3 13.4 3 4c0-.6.4-1 1-1h3.5c.6 0 1 .4 1 1 0 1.3.2 2.5.6 3.6.1.3 0 .7-.2 1z"/></svg>
      <span>11 6350-2481</span>
    </div>
    <div class="contact-row">
      <svg viewBox="0 0 24 24"><path d="M12 2C8.1 2 5 5.1 5 9c0 5.2 7 13 7 13s7-7.8 7-13c0-3.9-3.1-7-7-7zm0 9.5a2.5 2.5 0 1 1 0-5 2.5 2.5 0 0 1 0 5z"/></svg>
      <span>Al. Itapeva, 47, 3 andar<br>Alphaville | Barueri/ SP</span>
    </div>
  </div>

  <div class="contact contact-saopaulo">
    <div class="contact-row">
      <svg viewBox="0 0 24 24"><path d="M6.6 10.8c1.4 2.8 3.8 5.1 6.6 6.6l2.2-2.2c.3-.3.7-.4 1-.2 1.1.4 2.3.6 3.6.6.6 0 1 .4 1 1V20c0 .6-.4 1-1 1C10.6 21 3 13.4 3 4c0-.6.4-1 1-1h3.5c.6 0 1 .4 1 1 0 1.3.2 2.5.6 3.6.1.3 0 .7-.2 1z"/></svg>
      <span>11 4172-5036</span>
    </div>
    <div class="contact-row">
      <svg viewBox="0 0 24 24"><path d="M12 2C8.1 2 5 5.1 5 9c0 5.2 7 13 7 13s7-7.8 7-13c0-3.9-3.1-7-7-7zm0 9.5a2.5 2.5 0 1 1 0-5 2.5 2.5 0 0 1 0 5z"/></svg>
      <span>Av Dr Teixeira Lopes,<br>2710, sala 305, Vila Olímpia | São Paulo</span>
    </div>
  </div>
</section>

<section class="card card-back">
  <p class="back-name">Renato Bastiani</p>
  <p class="website">www.renatobastiani.com</p>
</section>

</body>
</html>
```